Kelvane Plumbing Business cards

Company is Kelvane Plumbing.
name Dashel Morrowby, I am a plumber, drainer, gasfitter and roofer
Mobile: 0431 906 154
Email address: info@kelvaneplumbing.example (check out my website for some ideas)
Website: www.kelvaneplumbing.example
ABN: 82 916 203 471
LIC: 604517K

I am reliable all round plumber. I am a 24 hour emergency service. Kelvane Plumbing is a professional plumbing service in the Illawarra, South Coast, Southern Sydney and Southern Highland regions of NSW. We offer a 24 hour emergency service for piece of mind to our customers. Call us now to see how we can help you. Kelvane Plumbing approaches every job with attention to detail and excellent customer service. With our superior workmanship you can be confident that the job will be done right the first time around. You can rest assured with results that are guaranteed to last.

Target Market(s)

the general public

Contact Information for Business Card

look up website for some ideas something with similar colours to logo and new modern and to catch the eye.

Colors
fdfdfd
ffffff
000000
7f7f7f
aaaaaa
33a6d7
0492cd

Requirements
Must have
• all contact details
• company- Kelvane Plumbing
• name- Dashel Morrowby
• number mobile- 0431 906 154
• Email address- info@kelvaneplumbing.example
• Website- www.kelvaneplumbing.example
• ABN- 82 916 203 471
• LIC- 604517K

```html
<!DOCTYPE html>
<html lang="en">
<head>
<meta charset="utf-8">
<title>Kelvane Plumbing – Business Card</title>
<link rel="stylesheet" href="https://fonts.googleapis.com/css2?family=Arimo:wght@400;700&display=swap">
<style>
  :root {
    --stage: #ececec;
    --card: #ffffff;
    --grey: #7f7f7f;
    --grey-light: #aaaaaa;
    --blue: #0492cd;
    --blue-soft: #33a6d7;
    --white: #fdfdfd;
    --ink: #000000;
  }
  html, body {
    margin: 0;
    padding: 0;
    width: 1200px;
    height: 900px;
    overflow: hidden;
    background: var(--stage);
    font-family: "Arimo", Arial, sans-serif;
  }
  .business-card {
    position: absolute;
    left: 100px;
    top: 180px;
    width: 1000px;
    height: 540px;
    background: var(--card);
    box-shadow: 0 6px 22px rgba(0,0,0,0.12);
    overflow: hidden;
  }
  .contact-panel {
    position: absolute;
    left: 0;
    top: 0;
    width: 455px;
    height: 540px;
  }
  .panel-shapes {
    position: absolute;
    inset: 0;
  }
  .holder-name {
    position: absolute;
    left: 58px;
    top: 34px;
    margin: 0;
    font-size: 28px;
    font-weight: 700;
    color: var(--white);
  }
  .registration {
    position: absolute;
    left: 58px;
    top: 326px;
    margin: 0;
    color: var(--white);
    font-size: 20px;
    line-height: 26px;
  }
  .registration dt {
    display: inline;
    font-weight: 700;
  }
  .registration dd {
    display: inline;
    margin: 0;
  }
  .contact-list {
    position: absolute;
    left: 46px;
    top: 428px;
    margin: 0;
    padding: 0;
    list-style: none;
    color: var(--white);
    font-size: 19px;
  }
  .contact-list li {
    display: flex;
    align-items: center;
    height: 30px;
  }
  .contact-icon {
    width: 22px;
    height: 22px;
    margin-right: 18px;
    flex: none;
  }
  .brand-panel {
    position: absolute;
    left: 455px;
    top: 0;
    width: 545px;
    height: 540px;
    display: flex;
    align-items: center;
    justify-content: center;
  }
  .brand-mark {
    display: flex;
    align-items: center;
    gap: 16px;
  }
  .brand-dot {
    width: 26px;
    height: 26px;
    border-radius: 50%;
    background: var(--grey);
  }
  .brand-name {
    margin: 0;
    font-size: 36px;
    font-weight: 700;
    color: var(--blue);
  }
</style>
</head>
<body>
  <article class="business-card">
    <section class="contact-panel">
      <svg class="panel-shapes" width="455" height="540" viewBox="0 0 455 540" aria-hidden="true">
        <polygon points="0,0 455,0 455,112 0,104" fill="var(--grey)"/>
        <polygon points="0,116 455,158 455,540 0,540" fill="var(--blue)"/>
      </svg>
      <h1 class="holder-name">Dashel Morrowby</h1>
      <dl class="registration">
        <div><dt>ABN:</dt> <dd>82 916 203 471</dd></div>
        <div><dt>LIC:</dt> <dd>604517K</dd></div>
      </dl>
      <ul class="contact-list">
        <li>
          <svg class="contact-icon" viewBox="0 0 22 22" aria-hidden="true">
            <rect x="6" y="1.5" width="10" height="19" rx="2" fill="none" stroke="var(--white)" stroke-width="1.8"/>
            <circle cx="11" cy="17" r="1.1" fill="var(--white)"/>
          </svg>
          <span>0431 906 154</span>
        </li>
        <li>
          <svg class="contact-icon" viewBox="0 0 22 22" aria-hidden="true">
            <rect x="2" y="5" width="18" height="12" fill="none" stroke="var(--white)" stroke-width="1.8"/>
            <polyline points="2,5 11,12 20,5" fill="none" stroke="var(--white)" stroke-width="1.8"/>
          </svg>
          <span>info@kelvaneplumbing.example</span>
        </li>
        <li>
          <svg class="contact-icon" viewBox="0 0 22 22" aria-hidden="true">
            <circle cx="11" cy="11" r="9" fill="none" stroke="var(--white)" stroke-width="1.6"/>
            <ellipse cx="11" cy="11" rx="4" ry="9" fill="none" stroke="var(--white)" stroke-width="1.4"/>
            <line x1="2" y1="11" x2="20" y2="11" stroke="var(--white)" stroke-width="1.4"/>
            <line x1="4" y1="6.5" x2="18" y2="6.5" stroke="var(--white)" stroke-width="1.2"/>
            <line x1="4" y1="15.5" x2="18" y2="15.5" stroke="var(--white)" stroke-width="1.2"/>
          </svg>
          <span>www.kelvaneplumbing.example</span>
        </li>
      </ul>
    </section>
    <section class="brand-panel">
      <div class="brand-mark">
        <span class="brand-dot" aria-hidden="true"></span>
        <p class="brand-name">Kelvane Plumbing</p>
      </div>
    </section>
  </article>
</body>
</html>
```